A New and modern Business Card for Tarvish Commerce Partners Ltd

New and modern Logo and Business Card Attached is the current logo/business card designCurrently the business is called "Tarvish & Co." or TCP Ltd for short. This is subject to change.This business specialises in Telecoms and Energy. We work with the major networks (QX, Z7, etc) and also offer Energy Products saving clients money off their energy bills.These are business to business services.The current design incorporates a Pheonix, indicating rebirth, starting something new.We would like to maintain the Phoenix element but a newer modern style.We love colours in the logo 3 max.The aim of this is to be ultra slick and modern. I envisage Tarvish & Co. on one side of the card with long descriptions on the other side.Side 1:TCP Ltd/Logo?Side 2:TCP Ltd/Logo/Graphic?Brogan & Co.Name:Address:Phone:Email:The design is mostly flexible but must incorporate a Phoenix.For example "Tarvish & Co." with a block phoenix behind the text...up to you.

Industry/Entity Type

Telecommunications

Contact Information for Business Card

Tarvish & Co.
Address:
Name:
Phone:
Email:

Logo Text

Tarvish & Co.

Colors
33a6d7
0792cd
acd037
9bcb3c
f78f20
fece3e

Requirements
Must have
• Phoenix
• 3/4 colours max
• Blue representing Technology (wireless)
• Green for Eco Energy
• Orange for Phoenix
• White business card background
Should not have
• phoenix must not all be red/ orange fire, we are a technology service company and the phoenix colours must represent this. Fire is not representative of our company.

```html
<!DOCTYPE html>
<html lang="en">
<head>
<meta charset="UTF-8">
<title>Tarvish &amp; Co. Business Card</title>
<link href="https://fonts.googleapis.com/css2?family=Work+Sans:wght@300;400&family=Arimo:wght@400;700&display=swap" rel="stylesheet">
<style>
  :root {
    --backdrop: #d9d9d9;
    --card-dark: #4a4b4f;
    --card-light: #ffffff;
    --brand-blue: #213f8f;
    --brand-green: #acd037;
    --brand-orange: #f7a144;
    --text-grey: #4a4a4a;
    --mark-white: #ffffff;
    --mark-dark: #4a4b4f;
  }
  * { margin: 0; padding: 0; box-sizing: border-box; }
  html, body {
    width: 1200px; height: 930px; overflow: hidden;
    background: var(--backdrop);
  }
  .canvas {
    position: relative; width: 1200px; height: 930px;
  }
  .card {
    position: absolute; left: 290px; width: 620px; height: 354px;
    box-shadow: 0 6px 18px rgba(0,0,0,0.18);
    overflow: hidden;
  }
  .card--front { top: 72px; background: var(--card-dark); }
  .card--back { top: 504px; background: var(--card-light); }

  .wordmark {
    position: absolute; display: flex; align-items: center; gap: 14px;
    font-family: "Work Sans", sans-serif; font-weight: 300;
    white-space: nowrap; letter-spacing: 1px;
  }
  .wordmark__square { display: block; }
  .card--front .wordmark {
    left: 50%; top: 50%; transform: translate(-50%, -50%);
    font-size: 50px; color: var(--mark-white);
  }
  .card--front .wordmark__square { width: 34px; height: 34px; background: var(--mark-white); }
  .card--back .wordmark {
    right: 44px; top: 40px; font-size: 34px; color: var(--mark-dark);
  }
  .card--back .wordmark__square { width: 24px; height: 24px; background: var(--mark-dark); }

  .person { position: absolute; left: 40px; top: 128px; font-family: "Arimo", sans-serif; }
  .person__name { font-weight: 700; font-size: 23px; color: var(--brand-blue); letter-spacing: 0.3px; }
  .person__role { font-weight: 400; font-size: 14px; color: var(--text-grey); margin-top: 3px; margin-left: 16px; }

  .divider {
    position: absolute; left: 56px; right: 44px; top: 186px;
    height: 1.5px; background: var(--brand-blue);
  }

  .contacts {
    position: absolute; left: 60px; top: 204px; list-style: none;
    font-family: "Arimo", sans-serif; font-size: 14.5px; color: var(--text-grey);
  }
  .contacts li { display: flex; align-items: center; gap: 12px; height: 23px; }
  .contacts svg { width: 12px; height: 12px; flex: none; }

  .address {
    position: absolute; right: 40px; top: 212px; text-align: right;
    font-family: "Arimo", sans-serif; font-size: 14px; line-height: 20px; color: var(--text-grey);
  }

  .band { position: absolute; left: 0; right: 0; bottom: 0; height: 10px; display: flex; }
  .band__green { width: 35%; background: var(--brand-green); }
  .band__blue { width: 33%; background: var(--brand-blue); }
  .band__orange { flex: 1; background: var(--brand-orange); }
</style>
</head>
<body>
<main class="canvas">
  <section class="card card--front">
    <div class="wordmark"><span class="wordmark__square"></span>Tarvish &amp; Co.</div>
  </section>

  <section class="card card--back">
    <div class="wordmark"><span class="wordmark__square"></span>Tarvish &amp; Co.</div>

    <div class="person">
      <div class="person__name">DANIEL OKAFOR</div>
      <div class="person__role">Director</div>
    </div>

    <div class="divider"></div>

    <ul class="contacts">
      <li>
        <svg viewBox="0 0 12 12" aria-hidden="true"><path d="M2.5 1h2l1 3-1.3 1a6 6 0 0 0 2.8 2.8L8 6.5l3 1v2c0 .8-.7 1.5-1.5 1.5A8.5 8.5 0 0 1 1 2.5C1 1.7 1.7 1 2.5 1z" fill="var(--brand-blue)"/></svg>
        <span>+612&nbsp; 9480 3172</span>
      </li>
      <li>
        <svg viewBox="0 0 12 12" aria-hidden="true"><rect x="3" y="1" width="6" height="4" fill="var(--brand-blue)"/><rect x="1" y="5" width="10" height="4" rx="1" fill="var(--brand-blue)"/><rect x="3" y="8" width="6" height="3" fill="var(--brand-blue)"/></svg>
        <span>+612&nbsp; 9480 3185</span>
      </li>
      <li>
        <svg viewBox="0 0 12 12" aria-hidden="true"><rect x="1" y="2.5" width="10" height="7" fill="none" stroke="var(--brand-blue)" stroke-width="1.3"/><path d="M1 2.5l5 4 5-4" fill="none" stroke="var(--brand-blue)" stroke-width="1.3"/></svg>
        <span>mail@tarvishco.com.au</span>
      </li>
      <li>
        <svg viewBox="0 0 12 12" aria-hidden="true"><circle cx="6" cy="6" r="5" fill="none" stroke="var(--brand-blue)" stroke-width="1.1"/><ellipse cx="6" cy="6" rx="2.2" ry="5" fill="none" stroke="var(--brand-blue)" stroke-width="1"/><path d="M1 6h10M2 3.5h8M2 8.5h8" stroke="var(--brand-blue)" stroke-width="0.9"/></svg>
        <span>www.tarvishco.com.au</span>
      </li>
    </ul>

    <div class="address">
      40-48 Harrow Lane<br>
      Sydney NSW 2000 Australia
    </div>

    <div class="band">
      <span class="band__green"></span>
      <span class="band__blue"></span>
      <span class="band__orange"></span>
    </div>
  </section>
</main>
</body>
</html>
```